Varnel Supply requires a new business card.

We are an online professional tool store.

Target Market(s)

We target the professional technician.

Industry/Entity Type

Business

Contact Information for Business Card

VarnelSupply.com.au

sales@varnelsupply.example

Requirements
Must have
• Needs to look commercial and professional
Should not have
• No Australian Colors, maps or shapes.
• No Shapes of Tools

```html
<!DOCTYPE html>
<html lang="en">
<head>
<meta charset="utf-8">
<title>Varnel Supply — Business Card</title>
<link href="https://fonts.googleapis.com/css2?family=Lato:wght@400;700&display=swap" rel="stylesheet">
<style>
  :root {
    --royal: #1428c0;
    --royal-deep: #0d1fa8;
    --cyan: #2a9fd0;
    --ink: #2b2b2b;
    --muted: #555;
    --paper: #ffffff;
    --backdrop: #3a3a3a;
  }
  html, body {
    margin: 0;
    width: 1200px;
    height: 900px;
    overflow: hidden;
    background: var(--backdrop);
    font-family: "Lato", sans-serif;
  }
  .sheet {
    width: 1200px;
    height: 900px;
    display: flex;
    flex-direction: column;
    align-items: center;
    justify-content: center;
    gap: 40px;
  }
  .card {
    position: relative;
    width: 680px;
    height: 390px;
    box-sizing: border-box;
    overflow: hidden;
    box-shadow: 0 10px 30px rgba(0,0,0,.35);
  }

  /* Front */
  .card--front { background: var(--paper); color: var(--ink); }
  .holder { position: absolute; left: 46px; top: 40px; }
  .holder__name {
    margin: 0;
    font-size: 28px;
    font-weight: 700;
    color: var(--royal);
    letter-spacing: -0.3px;
  }
  .holder__role { margin: 2px 0 0; font-size: 15px; color: var(--muted); }
  .contact {
    position: absolute;
    left: 46px;
    top: 135px;
    font-size: 16px;
    line-height: 23px;
    color: var(--ink);
  }
  .contact p { margin: 0; }
  .contact__address { margin-bottom: 8px !important; }
  .contact__line { display: flex; align-items: center; gap: 9px; }
  .contact__icon { width: 13px; height: 13px; flex: none; }

  .brand {
    position: absolute;
    display: flex;
    align-items: center;
    gap: 12px;
    font-weight: 700;
    color: var(--royal);
  }
  .brand__dot { border-radius: 50%; background: currentColor; flex: none; }
  .card--front .brand { right: 56px; top: 150px; font-size: 34px; }
  .card--front .brand__dot { width: 22px; height: 22px; }

  .edge-band { position: absolute; left: 0; bottom: 0; width: 680px; height: 44px; }
  .edge-band__url {
    position: absolute;
    left: 46px;
    bottom: 11px;
    font-size: 16px;
    color: var(--paper);
    letter-spacing: 0.2px;
  }

  /* Back */
  .card--back { background: var(--royal); color: var(--paper); }
  .card--back .brand {
    left: 0; right: 0; top: 150px;
    justify-content: center;
    font-size: 44px;
    color: var(--paper);
  }
  .card--back .brand__dot { width: 28px; height: 28px; }
  .back__url {
    position: absolute;
    left: 0; right: 0; top: 252px;
    text-align: center;
    font-size: 17px;
    letter-spacing: 0.3px;
    margin: 0;
  }
</style>
</head>
<body>
<main class="sheet">

  <section class="card card--front" aria-label="Business card front">
    <div class="holder">
      <h1 class="holder__name">Dalen Prewitt</h1>
      <p class="holder__role">Manager</p>
    </div>

    <div class="contact">
      <p class="contact__address">418 Corlew Lane<br>Brantfield, TX 77512</p>
      <p class="contact__line">
        <svg class="contact__icon" viewBox="0 0 16 16" aria-hidden="true"><path fill="#1428c0" d="M4 1l3 3-2 2c1 2 3 4 5 5l2-2 3 3-2 3C7 15 1 9 1 3z"/></svg>
        555 014 2280
      </p>
      <p class="contact__line">
        <svg class="contact__icon" viewBox="0 0 16 16" aria-hidden="true"><rect x="4" y="1" width="8" height="5" fill="#1428c0"/><rect x="1" y="6" width="14" height="7" rx="1" fill="#1428c0"/><rect x="4" y="10" width="8" height="5" fill="#fff" stroke="#1428c0"/></svg>
        555 014 2281
      </p>
      <p class="contact__line">
        <svg class="contact__icon" viewBox="0 0 16 16" aria-hidden="true"><rect x="1" y="3" width="14" height="10" fill="#1428c0"/><path d="M1 3l7 6 7-6" fill="none" stroke="#fff" stroke-width="1.4"/></svg>
        sales@varnelsupply.example
      </p>
    </div>

    <div class="brand"><span class="brand__dot"></span>Varnel Supply</div>

    <svg class="edge-band" viewBox="0 0 680 44" aria-hidden="true">
      <polygon points="0,14 560,14 540,44 0,44" fill="#1428c0"/>
      <polygon points="572,0 612,0 590,30 550,30" fill="#2a9fd0"/>
      <polygon points="620,14 680,14 680,44 600,44" fill="#1428c0"/>
    </svg>
    <span class="edge-band__url">www.varnelsupply.com.au</span>
  </section>

  <section class="card card--back" aria-label="Business card back">
    <div class="brand"><span class="brand__dot"></span>Varnel Supply</div>
    <p class="back__url">www.varnelsupply.com.au</p>
  </section>

</main>
</body>
</html>
```